Corwin Hale

20 Year Licensed Master Barber specializing in:
men/women cuts, Grooming, Straight razor Shaving and tape line enhancement, beard grooming, eye brow enhancement, South of France, Hot Towel Treatments, Scalp, Blow outs, Shags, Custom Design,RazorCuts,Shear Cuts, Bobs, Perms, Relaxers, Shoe Shine.
Please create a wonderful business card incorporating all the info above and selecting one of the photos. Please be creative.

Barber

```html
<!DOCTYPE html>
<html lang="en">
<head>
<meta charset="utf-8">
<title>Corwin Hale – Master Barber Business Card</title>
<link rel="stylesheet" href="https://fonts.googleapis.com/css2?family=Oswald:wght@500&family=Saira:wght@400;500;600&display=swap">
<style>
  :root {
    --page-bg: #e9e9ec;
    --card-top: #f4f4f6;
    --card-bottom: #dcdde0;
    --band-blue: #3b3a9c;
    --band-blue-dark: #2f2e86;
    --silver-light: #f7f7f9;
    --silver-dark: #9c9ea4;
    --footer-top: #e6e6e8;
    --footer-bottom: #c9c9cc;
    --white: #ffffff;
    --ink: #2b2b33;
    --icon-ink: #3b3a9c;
    --logo-ring: #3b3a9c;
    --logo-text: #3b3a9c;
  }
  * { box-sizing: border-box; margin: 0; padding: 0; }
  html, body {
    width: 1200px; height: 768px; overflow: hidden;
    background: var(--page-bg);
  }
  .card {
    position: absolute; left: 80px; top: 64px;
    width: 1040px; height: 640px;
    background: linear-gradient(180deg, var(--card-top), var(--card-bottom));
    box-shadow: 0 10px 30px rgba(0,0,0,.15);
    overflow: hidden;
  }
  .brand {
    position: absolute; left: 0; right: 0; top: 36px;
    display: flex; justify-content: center;
  }
  .brand-mark {
    width: 140px; height: 140px; border-radius: 50%;
    border: 4px solid var(--logo-ring);
    background: var(--white);
    display: flex; align-items: center; justify-content: center;
    text-align: center;
  }
  .brand-name {
    font-family: "Saira", sans-serif; font-weight: 600;
    font-size: 24px; line-height: 1.05; color: var(--logo-text);
    text-transform: uppercase;
  }
  .rule {
    position: absolute; left: 0; right: 0; height: 6px;
    background: linear-gradient(90deg, var(--silver-dark), var(--silver-light) 30%, var(--silver-dark) 55%, var(--silver-light) 80%, var(--silver-dark));
  }
  .rule-top { top: 199px; }
  .rule-mid { top: 455px; }
  .rule-bottom { top: 545px; }
  .contact-band {
    position: absolute; left: 0; right: 0; top: 205px; height: 250px;
    background: linear-gradient(180deg, var(--band-blue), var(--band-blue-dark));
    display: grid; grid-template-columns: repeat(3, 1fr);
    padding: 0 40px;
  }
  .contact-item {
    display: flex; flex-direction: column; align-items: center;
    padding-top: 40px; color: var(--white); text-align: center;
  }
  .contact-icon {
    width: 92px; height: 92px; border-radius: 50%;
    background: var(--white);
    border: 4px solid #c7c8d6;
    display: flex; align-items: center; justify-content: center;
    margin-bottom: 26px;
  }
  .holder-name {
    font-family: "Oswald", sans-serif; font-weight: 500;
    font-size: 44px; line-height: 1; letter-spacing: 1px;
    white-space: nowrap;
  }
  .holder-title {
    font-family: "Saira", sans-serif; font-size: 14px;
    letter-spacing: 1px; margin-top: 4px;
  }
  .contact-line {
    font-family: "Saira", sans-serif; font-size: 22px;
    line-height: 1.4; letter-spacing: .3px; white-space: nowrap;
  }
  .social-bar {
    position: absolute; left: 0; right: 0; top: 461px; height: 84px;
    background: linear-gradient(180deg, var(--footer-top), var(--footer-bottom));
    display: flex; align-items: center; padding-left: 96px;
  }
  .follow { color: var(--ink); margin-right: 40px; }
  .follow-title {
    font-family: "Saira", sans-serif; font-weight: 500;
    font-size: 28px; letter-spacing: 2px; line-height: 1;
  }
  .follow-sub {
    font-family: "Saira", sans-serif; font-size: 11px;
    letter-spacing: 1px; margin-top: 6px;
  }
  .social-list { display: flex; gap: 22px; }
  .social-dot {
    width: 30px; height: 30px; border-radius: 50%;
    background: var(--ink);
  }
  .services {
    position: absolute; left: 0; right: 0; top: 551px; height: 89px;
    padding: 10px 60px 0;
    text-align: center; color: var(--ink);
    font-family: "Saira", sans-serif; font-size: 13.5px; line-height: 1.4;
  }
  .services-title {
    font-weight: 600; color: var(--band-blue); letter-spacing: .5px;
  }
</style>
</head>
<body>
  <div class="card">
    <div class="brand">
      <div class="brand-mark">
        <span class="brand-name">Corwin<br>Hale</span>
      </div>
    </div>

    <div class="rule rule-top"></div>

    <div class="contact-band">
      <div class="contact-item">
        <div class="contact-icon">
          <svg width="48" height="48" viewBox="0 0 48 48" aria-hidden="true">
            <circle cx="24" cy="16" r="9" fill="var(--icon-ink)"/>
            <path d="M7 44c0-10 8-16 17-16s17 6 17 16z" fill="var(--icon-ink)"/>
          </svg>
        </div>
        <div class="holder-name">CORWIN HALE</div>
        <div class="holder-title">LICENSED MASTER BARBER</div>
      </div>
      <div class="contact-item">
        <div class="contact-icon">
          <svg width="52" height="52" viewBox="0 0 52 52" aria-hidden="true" fill="none" stroke="var(--icon-ink)" stroke-width="3">
            <circle cx="26" cy="26" r="21"/>
            <ellipse cx="26" cy="26" rx="9" ry="21"/>
            <line x1="5" y1="26" x2="47" y2="26"/>
            <line x1="26" y1="5" x2="26" y2="47"/>
            <path d="M9 15h34M9 37h34"/>
          </svg>
        </div>
        <div class="contact-line">corwin@halebarbers.com</div>
        <div class="contact-line">www.halebarbers.com</div>
      </div>
      <div class="contact-item">
        <div class="contact-icon">
          <svg width="40" height="52" viewBox="0 0 40 52" aria-hidden="true">
            <rect x="6" y="2" width="28" height="48" rx="4" fill="var(--icon-ink)"/>
            <rect x="10" y="9" width="20" height="30" fill="var(--white)"/>
            <circle cx="20" cy="44" r="2.5" fill="var(--white)"/>
          </svg>
        </div>
        <div class="contact-line">555 214 3370</div>
        <div class="contact-line">555 214 3371</div>
      </div>
    </div>

    <div class="rule rule-mid"></div>

    <div class="social-bar">
      <div class="follow">
        <div class="follow-title">FOLLOW US</div>
        <div class="follow-sub">ON SOCIAL NETWORKS</div>
      </div>
      <div class="social-list">
        <span class="social-dot"></span>
        <span class="social-dot"></span>
        <span class="social-dot"></span>
        <span class="social-dot"></span>
      </div>
    </div>

    <div class="rule rule-bottom"></div>

    <div class="services">
      <span class="services-title">20 Year Licensed Master Barber specializing in:</span>
      men/women cuts, Grooming, Straight Razor Shaving and tape line enhancement, beard grooming, eye brow enhancement,
      South of France, Hot Towel Treatments, Scalp, Blow outs, Shags, Custom Design, Razor Cuts, Shear Cuts, Bobs, Perms, Relaxers, Shoe Shine.
    </div>
  </div>
</body>
</html>
```